Tarvik Plans - Worpress Design

We are a consultancy to help builders to optimize their planning in order to save building costs. For that reason we need a website to offer our services, present our history, the mission and offer a plug-in for a first contact (including calendar), testimonials, a blog etc.
As an idea, I really like: https://www.fendrowadvisory.de/
Later on the website should be programmed in www.quelvo.de in our Wordpress area. The text, of course, will be done by myself. The colors should be suitable to our recently designed logo.

```html
<!DOCTYPE html>
<html lang="en">
<head>
<meta charset="utf-8">
<title>Tarvik Plans</title>
<link rel="stylesheet" href="https://fonts.googleapis.com/css2?family=Orbitron:wght@700;900&family=Poppins:wght@400;500;600;700&display=swap">
<style>
:root{
  --gold-1:#b9852a;
  --gold-2:#e6c36c;
  --gold:#c9973c;
  --ink:#2a2c33;
  --dark-1:#25272d;
  --dark-2:#4a4c55;
  --text:#555860;
  --muted:#8b8d93;
  --soft:#f3f3f4;
  --line:#e3e3e5;
  --white:#ffffff;
}
*{margin:0;padding:0;box-sizing:border-box}
html,body{width:1200px;height:4630px;overflow:hidden;background:var(--white)}
body{font-family:"Poppins",sans-serif;color:var(--text)}
.page{position:relative;width:1200px;height:4630px;overflow:hidden}
.abs{position:absolute}
.display{font-family:"Orbitron",sans-serif;font-weight:900;color:var(--ink);letter-spacing:1px}
.btn-gold{position:absolute;display:flex;align-items:center;justify-content:center;background:linear-gradient(90deg,var(--gold-1),var(--gold-2));color:var(--white);font-size:11px;font-weight:600;letter-spacing:.5px;text-transform:uppercase}
.photo{position:absolute}

/* header */
.brand{position:absolute;left:92px;top:30px;display:flex;align-items:center;gap:12px;font-family:"Poppins",sans-serif;font-weight:700;font-size:26px;color:var(--gold-2);letter-spacing:1px}
.brand-mark{width:30px;height:30px;border:2px solid var(--gold-2)}
.nav{position:absolute;top:36px;left:584px;display:flex;gap:30px;font-size:11px;font-weight:500;color:var(--white)}
.nav .active{color:var(--gold-2)}
.nav-cta{position:absolute;left:993px;top:27px;width:117px;height:36px;border:2px solid var(--white);color:var(--white);font-size:11px;font-weight:600;display:flex;align-items:center;justify-content:center}

/* hero */
.hero-title{position:absolute;left:86px;top:215px;font-family:"Orbitron",sans-serif;font-weight:900;font-size:72px;line-height:76px;color:var(--white)}
.hero-title .gold{color:var(--gold)}
.hero-sub{position:absolute;left:88px;top:377px;font-size:15px;color:var(--white);font-weight:500}
.scroll-label{position:absolute;left:608px;top:664px;font-size:9px;font-weight:600;color:var(--ink);transform:rotate(90deg);transform-origin:left top;letter-spacing:1px}

/* section titles */
.section-title{position:absolute;left:0;width:1200px;text-align:center;font-size:36px}

/* cards */
.card{position:absolute;width:286px}
.card-body{background:var(--soft);clip-path:polygon(0 0,100% 0,100% 88%,0 100%);padding:24px 30px 0}
.card h3{font-size:13px;font-weight:700;color:var(--ink);text-transform:uppercase;margin-bottom:10px}
.card p{font-size:12px;line-height:19px;color:var(--text)}
.arrow{display:block;margin-top:20px}
.meta{display:flex;gap:20px;font-size:10px;color:var(--muted);margin-bottom:12px;align-items:center}
.meta span{display:flex;align-items:center;gap:6px}
.tag{position:absolute;z-index:2;left:30px;top:220px;background:linear-gradient(90deg,var(--gold-1),var(--gold-2));color:var(--white);font-size:9px;font-weight:600;padding:2px 10px;line-height:14px}

/* mission / history */
.copy{position:absolute;font-size:12.5px;line-height:20.5px}
.history-copy{color:#e9e9ec}

/* testimonial */
.quote-mark{position:absolute;left:90px;top:2610px;font-family:Georgia,serif;font-size:340px;line-height:1;color:#efeff0}
.quote-text{position:absolute;left:230px;width:740px;top:2768px;text-align:center;font-size:14.5px;line-height:25px;color:var(--text)}
.stars{position:absolute;left:0;width:1200px;top:2852px;text-align:center;color:var(--gold);font-size:13px;letter-spacing:1px}
.quote-name{position:absolute;left:0;width:1200px;top:2880px;text-align:center;font-size:11.5px;font-weight:600;color:var(--ink)}

/* contact */
.label{position:absolute;font-size:10.5px;font-weight:700;color:var(--ink)}
.field{position:absolute;background:var(--soft);font-size:11px;color:var(--muted);padding:0 14px;display:flex;align-items:center}
.submit{position:absolute;left:167px;top:3946px;width:417px;height:47px;background:linear-gradient(90deg,var(--gold-1),var(--gold-2));color:var(--white);font-weight:700;font-size:14px;display:flex;align-items:center;justify-content:center}
.calendar{position:absolute;left:650px;top:3660px;width:388px;height:336px;background:var(--white);box-shadow:0 10px 40px rgba(0,0,0,.09)}
.cal-month{position:absolute;left:34px;top:36px;font-size:26px}
.cal-year{position:absolute;left:34px;top:76px;font-size:17px;color:var(--ink);font-weight:500}
.cal-day{position:absolute;left:245px;top:0;width:108px;height:81px;background:linear-gradient(135deg,var(--gold-1),var(--gold-2));color:var(--white);font-family:"Orbitron",sans-serif;font-weight:900;font-size:30px;display:flex;align-items:flex-end;justify-content:center;padding-bottom:10px}
.cal-grid{position:absolute;left:20px;top:120px;width:350px;display:grid;grid-template-columns:repeat(7,1fr);row-gap:14px;text-align:center;font-size:14px;color:#9a9ca2}
.cal-grid .head{font-size:11px;font-weight:700;color:var(--ink);margin-bottom:18px}

/* footer */
.foot-head{position:absolute;top:4320px;font-size:13px;font-weight:700;color:var(--white)}
.foot-list{position:absolute;font-size:12px;color:#d4d5d8;line-height:27px;list-style:none}
.foot-text{position:absolute;font-size:11.5px;color:#d4d5d8;line-height:17px}
.social{position:absolute;top:4432px;width:34px;height:34px;border-radius:50%;border:1px solid #6b6d74}
.copyright{position:absolute;top:4592px;left:0;width:1200px;text-align:center;font-size:11px;color:#e0e0e3;font-weight:500}
</style>
</head>
<body>
<div class="page">

  <!-- hero -->
  <div class="photo" role="img" aria-label="Team of business people in suits meeting around a laptop in an office" style="left:0;top:0;width:1200px;height:900px;background:linear-gradient(100deg,#1f2024 0%,#3d3e43 35%,#6f6b66 60%,#8a8782 100%)"></div>
  <svg class="abs" style="left:0;top:0" width="1200" height="900" aria-hidden="true">
    <polygon points="560,650 1200,735 1200,900" fill="#e6e6e8"/>
    <polygon points="0,557 1200,848 1200,900 0,900" fill="#ffffff"/>
    <polygon points="532,647 668,647 600,772" fill="#ffffff"/>
    <polyline points="595,715 600,721 605,715" fill="none" stroke="#2a2c33" stroke-width="1.6"/>
  </svg>
  <div class="scroll-label">SCROLL</div>

  <div class="brand"><span class="brand-mark"></span>TARVIK PLANS</div>
  <nav class="nav"><span class="active">HOME</span><span>OUR HISTORY</span><span>SERVICES</span><span>MISSION</span><span>BLOG</span></nav>
  <div class="nav-cta">CONTACT US</div>

  <h1 class="hero-title"><span class="gold">TARVIK</span><br>PLANS</h1>
  <p class="hero-sub">PLANNING IN ORDER TO SAVE BUILDING COSTS</p>
  <div class="btn-gold" style="left:88px;top:424px;width:140px;height:38px">GET IN TOUCH</div>

  <!-- services -->
  <h2 class="display section-title" style="top:838px">SERVICES</h2>

  <div class="card" style="left:153px;top:903px">
    <div role="img" aria-label="Trainer presenting at a flip chart to a seated group" style="height:228px;background:linear-gradient(135deg,#7c7f84,#d8d9db)"></div>
    <div class="card-body" style="height:184px">
      <h3>Training and Workshops</h3>
      <p>Offering training sessions and workshops to builders and their teams on cost optimization...</p>
      <svg class="arrow" width="22" height="12"><path d="M0 6H20M15 1l5 5-5 5" stroke="#2a2c33" stroke-width="1.5" fill="none"/></svg>
    </div>
  </div>
  <div class="card" style="left:456px;top:903px">
    <div role="img" aria-label="Engineers in hard hats reviewing plans on site" style="height:228px;background:linear-gradient(135deg,#5f6368,#c9cbcf)"></div>
    <div class="card-body" style="height:184px">
      <h3>Regulatory Compliance</h3>
      <p>Assisting builders in navigating complex building regulations and compliance requirements...</p>
      <svg class="arrow" width="22" height="12"><path d="M0 6H20M15 1l5 5-5 5" stroke="#2a2c33" stroke-width="1.5" fill="none"/></svg>
    </div>
  </div>
  <div class="card" style="left:762px;top:903px">
    <div role="img" aria-label="Planners in hard hats studying blueprints at a table" style="height:228px;background:linear-gradient(135deg,#8a9aa8,#e4e8ec)"></div>
    <div class="card-body" style="height:184px">
      <h3>Cost Optimization</h3>
      <p>Assisting builders in identifying areas of potential cost savings throughout the building...</p>
      <svg class="arrow" width="22" height="12"><path d="M0 6H20M15 1l5 5-5 5" stroke="#2a2c33" stroke-width="1.5" fill="none"/></svg>
    </div>
  </div>
  <div class="btn-gold" style="left:540px;top:1360px;width:119px;height:36px">VIEW ALL</div>

  <!-- mission -->
  <h2 class="display abs" style="left:174px;top:1585px;font-size:34px">MISSION</h2>
  <p class="copy" style="left:176px;top:1638px;width:336px">Lorem Ipsum is simply dummy text of the printing and typesetting industry. Lorem Ipsum has been the industry's standard dummy text ever since the 1500s, when an unknown printer took a galley of type and scrambled it to make a type specimen book. It has survived not only five centuries, but also the...</p>
  <div class="btn-gold" style="left:176px;top:1802px;width:120px;height:34px">READ MORE</div>
  <div class="photo" role="img" aria-label="Business people in hard hats discussing a plan in a bright hall" style="left:550px;top:1485px;width:447px;height:458px;background:linear-gradient(135deg,#6d6f74,#c4c6ca 60%,#9a9ca0);clip-path:polygon(0 0,100% 0,100% 76%,0 100%)"></div>
  <svg class="abs" style="left:990px;top:1760px" width="50" height="150" aria-hidden="true"><polygon points="6,50 47,8 47,140" fill="#d9d9dc"/></svg>

  <!-- history -->
  <svg class="abs" style="left:0;top:1800px" width="1200" height="760" aria-hidden="true">
    <defs><linearGradient id="darkband" x1="0" y1="0" x2="1" y2="0"><stop offset="0" stop-color="#5a5c64"/><stop offset=".5" stop-color="#3a3c43"/><stop offset="1" stop-color="#25272d"/></linearGradient></defs>
    <polygon points="0,455 1200,140 1200,741 0,741" fill="url(#darkband)"/>
  </svg>
  <div class="photo" role="img" aria-label="Three smiling senior colleagues standing together" style="left:60px;top:2012px;width:695px;height:529px;background:linear-gradient(180deg,#9a9aa0 0%,#6c6e76 55%,#3e4047 100%);clip-path:polygon(8% 12%,92% 0,100% 100%,0 100%)"></div>
  <h2 class="display abs" style="left:796px;top:2140px;font-size:34px;line-height:40px;color:#fff">PRO<br>HISTORY</h2>
  <p class="copy history-copy" style="left:797px;top:2234px;width:320px">Lorem Ipsum is simply dummy text of the printing and typesetting industry. Lorem Ipsum has been the industry's standard dummy text ever since the 1500s, when an unknown printer took a galley of type and scrambled it to make a type specimen book. It has survived not only five centuries, but also the.</p>
  <div class="btn-gold" style="left:797px;top:2403px;width:121px;height:34px">READ MORE</div>

  <!-- testimonial -->
  <div class="photo" role="img" aria-label="Client portrait" style="left:460px;top:2641px;width:72px;height:72px;background:linear-gradient(135deg,#b58b6c,#6e4c3a)"></div>
  <div class="photo" role="img" aria-label="Featured client portrait" style="left:562px;top:2624px;width:104px;height:104px;background:linear-gradient(135deg,#8fa3b0,#3c3f46)"></div>
  <div class="photo" role="img" aria-label="Client portrait" style="left:694px;top:2641px;width:73px;height:73px;background:linear-gradient(135deg,#a9a29c,#5a524e)"></div>
  <div class="quote-mark">“</div>
  <p class="quote-text">Lorem Ipsum is simply dummy text of the printing and typesetting industry. Lorem Ipsum has been the industry's standard dummy text ever since the 1500s, when an unknown printer took a galley of type and scrambled it to make a type specimen ...</p>
  <div class="stars">★★★★<span style="color:#e4d3ad">★</span></div>
  <div class="quote-name">MARLA QUENBY</div>
  <div class="abs" style="left:88px;top:2951px;width:1024px;height:1px;background:var(--line)"></div>

  <!-- articles -->
  <h2 class="display section-title" style="top:3010px">ARTICLE</h2>

  <div class="card" style="left:153px;top:3071px">
    <div role="img" aria-label="Workers in hard hats unrolling building plans" style="height:230px;background:linear-gradient(135deg,#7e8690,#d2d6da)"></div>
    <span class="tag">STORY</span>
    <div class="card-body" style="height:200px">
      <h3>Blog heading goes here</h3>
      <div class="meta"><span>▦ 25-05-2023</span><span>◉ By John</span></div>
      <p>Lorem Ipsum is simply typesetting industry lorem Ipsum...</p>
      <svg class="arrow" width="22" height="12"><path d="M0 6H20M15 1l5 5-5 5" stroke="#2a2c33" stroke-width="1.5" fill="none"/></svg>
    </div>
  </div>
  <div class="card" style="left:456px;top:3071px">
    <div role="img" aria-label="Group of professionals in hard hats in a modern hall" style="height:230px;background:linear-gradient(135deg,#6a6d72,#cfd1d4)"></div>
    <span class="tag">STORY</span>
    <div class="card-body" style="height:200px">
      <h3>Blog heading goes here</h3>
      <div class="meta"><span>▦ 25-05-2023</span><span>◉ By John</span></div>
      <p>Lorem Ipsum is simply typesetting industry lorem Ipsum...</p>
      <svg class="arrow" width="22" height="12"><path d="M0 6H20M15 1l5 5-5 5" stroke="#2a2c33" stroke-width="1.5" fill="none"/></svg>
    </div>
  </div>
  <div class="card" style="left:762px;top:3071px">
    <div role="img" aria-label="Two engineers reviewing drawings in a bright workshop" style="height:230px;background:linear-gradient(135deg,#8b8e93,#e5e6e8)"></div>
    <span class="tag">STORY</span>
    <div class="card-body" style="height:200px">
      <h3>Blog heading goes here</h3>
      <div class="meta"><span>▦ 25-05-2023</span><span>◉ By John</span></div>
      <p>Lorem Ipsum is simply typesetting industry lorem Ipsum...</p>
      <svg class="arrow" width="22" height="12"><path d="M0 6H20M15 1l5 5-5 5" stroke="#2a2c33" stroke-width="1.5" fill="none"/></svg>
    </div>
  </div>

  <!-- contact -->
  <h2 class="display abs" style="left:167px;top:3580px;font-size:34px">CONTACT</h2>
  <div class="label" style="left:167px;top:3640px">NAME</div>
  <div class="field" style="left:167px;top:3662px;width:417px;height:40px">Enter your name</div>
  <div class="label" style="left:167px;top:3716px">EMAIL</div>
  <div class="field" style="left:167px;top:3738px;width:205px;height:38px">Enter your email</div>
  <div class="label" style="left:379px;top:3716px">TELEPHONE</div>
  <div class="field" style="left:379px;top:3738px;width:205px;height:38px">Enter phone number</div>
  <div class="label" style="left:167px;top:3786px">MESSAGE</div>
  <div class="field" style="left:167px;top:3806px;width:417px;height:111px;align-items:flex-start;padding-top:14px">Type your text...</div>
  <div class="submit">SUBMIT
    <svg style="position:absolute;right:20px;top:16px" width="16" height="16"><path d="M1 8L15 1 11 15 8 9z" fill="#fff"/></svg>
  </div>

  <div class="calendar">
    <div class="display cal-month">JANUARY <span style="font-size:14px">⇕</span></div>
    <div class="cal-year">2023</div>
    <div class="cal-day">01</div>
    <div class="cal-grid">
      <span class="head">SUN</span><span class="head">MON</span><span class="head">TUE</span><span class="head">WED</span><span class="head">THU</span><span class="head">FRI</span><span class="head">SAT</span>
      <span></span><span></span><span>01</span><span>02</span><span>03</span><span>04</span><span>05</span>
      <span>06</span><span>07</span><span>08</span><span>09</span><span>10</span><span>11</span><span>12</span>
      <span>13</span><span>14</span><span>15</span><span>16</span><span>17</span><span>18</span><span>19</span>
      <span>20</span><span>21</span><span>22</span><span>23</span><span>24</span><span>25</span><span>26</span>
      <span>27</span><span>28</span><span>29</span><span>30</span><span>31</span><span></span><span></span>
    </div>
  </div>

  <!-- footer -->
  <svg class="abs" style="left:0;top:4030px" width="1200" height="600" aria-hidden="true">
    <defs><linearGradient id="footband" x1="0" y1="0" x2="1" y2="1"><stop offset="0" stop-color="#3c3e45"/><stop offset="1" stop-color="#1f2126"/></linearGradient></defs>
    <polygon points="0,15 1200,160 1200,600 0,600" fill="url(#footband)"/>
    <polygon points="1128,500 1178,500 1153,460" fill="#c9973c"/>
    <path d="M1153 492V475M1147 481l6-6 6 6" stroke="#fff" stroke-width="1.3" fill="none"/>
  </svg>

  <div class="brand" style="left:93px;top:4370px;font-size:24px"><span class="brand-mark"></span>TARVIK PLANS</div>
  <span class="social" style="left:166px"></span>
  <span class="social" style="left:211px"></span>
  <span class="social" style="left:258px"></span>
  <span class="social" style="left:303px"></span>

  <div class="foot-head" style="left:476px">QUICK LINKS</div>
  <ul class="foot-list" style="left:476px;top:4358px"><li>Home</li><li>Our History</li><li>Services</li><li>Mission</li><li>Blog</li><li>Contact Us</li></ul>

  <div class="foot-head" style="left:641px">CONTACT INFO</div>
  <svg class="abs" style="left:641px;top:4362px" width="14" height="10"><rect x=".5" y=".5" width="13" height="9" fill="none" stroke="#c9973c"/><path d="M1 1l6 5 6-5" fill="none" stroke="#c9973c"/></svg>
  <p class="foot-text" style="left:664px;top:4358px">Email:<br>hello@tarvikplans.de</p>
  <svg class="abs" style="left:641px;top:4413px" width="13" height="13"><path d="M3 1l3 3-2 2c1 2 2 3 4 4l2-2 3 3-2 2C6 12 1 7 1 3z" fill="#c9973c"/></svg>
  <p class="foot-text" style="left:664px;top:4410px">Phone:<br>+49 30 5550 1842</p>
  <svg class="abs" style="left:642px;top:4465px" width="12" height="16"><path d="M6 15C2 10 1 8 1 6a5 5 0 0110 0c0 2-1 4-5 9z" fill="#c9973c"/><circle cx="6" cy="6" r="2" fill="#2a2c33"/></svg>
  <p class="foot-text" style="left:664px;top:4462px">Location:<br>Lindenweg 14,<br>10115 Berlin</p>

  <div class="foot-head" style="left:864px">NEWSLETTER</div>
  <p class="foot-text" style="left:864px;top:4360px;width:240px">Subscribe to our email address to get the latest news.</p>
  <div class="abs" style="left:864px;top:4416px;width:246px;height:45px;background:#3a3c43;display:flex;align-items:center;padding:0 16px;font-size:11.5px;color:#e0e0e3">✉&nbsp; Enter your email...</div>
  <svg class="abs" style="left:1080px;top:4431px" width="15" height="15"><path d="M1 7L14 1 10 14 7 8z" fill="#c9973c"/></svg>

  <div class="copyright">© 2023 Tarvik Plans, All Rights Reserved</div>
</div>
</body>
</html>
```